Corporate Wall Mural for Office

We have several offices across North America and we want to have a corporate wall mural in each office, so we require a mural wall design that can be adjusted for different wall dimensions and still look good.

The first mural will be 239.5" x 112.5" it will be in our Toronto office - so the background city will be the Toronto skyline

I have attached a draft design and the content PNG file.

We want a different design that keeps the content outlined in the Mural Design Content PNG file.

Our corporate font is Gilroy Semi Bold

Our corporate colors are
Blue
C94
M70
Y0
K12
Pantone 2945C

Purple
C 80
M 78
PMS 2368 C

Sky Blue
C68
M34
PMS 2727 C
Our website is qalverpoint.com

Founded in 2012, QPT is a leading provider of technology infrastructure solutions, specializing in Broadband, DAS/Private Networks, Fixed Wireless Access, Site Solutions, Carrier Networks, and Test & Measurement. Our mission is to empower organizations of all sizes with innovative connectivity and telecom infrastructure solutions to build the future of communications.

Target Market(s)

Target is the staff and visitors of our office

Industry/Entity Type

network infrastructure: both wireless and wireline

Font styles to use
Sans Serif
Other font styles liked:
• Gilroy Semi-Bold and Bold

Colors
0054AA
0677BA
7BADD7
CADEEF
E8F1F8

Requirements
Must have
• the info listed in the Mural Content.png file, our corporate colors. It should be bright and energetic.
Nice to have
• I like concept of the city silhouette from the draft design

```html
<!DOCTYPE html>
<html lang="en">
<head>
<meta charset="utf-8">
<title>QPT – Enabling Solutions for a Connected World</title>
<link rel="stylesheet" href="https://fonts.googleapis.com/css2?family=Roboto:ital,wght@0,300;0,400;0,500;0,700;1,900&display=swap">
<style>
  :root {
    --corp-blue: #1f4e9c;
    --corp-purple: #574aa0;
    --sky-blue: #5b93d0;
    --band-blue: #5590d0;
    --box-blue: rgba(52, 92, 165, 0.88);
    --box-purple: rgba(104, 90, 172, 0.92);
    --ink: #111827;
    --navy-ink: #14224a;
    --white: #ffffff;
  }
  * { box-sizing: border-box; margin: 0; padding: 0; }
  html, body { width: 1200px; height: 564px; overflow: hidden; background: #fff; }
  body { font-family: "Roboto", sans-serif; }

  .mural { position: relative; width: 1200px; height: 564px; overflow: hidden; }

  .skyline-scene {
    position: absolute; inset: 0;
    background:
      linear-gradient(180deg,
        #5e86b0 0%, #87a6c4 22%, #b9c3c9 42%,
        #e6cf9c 62%, #e6b57a 72%, #8aa3a6 80%,
        #4fa9b3 88%, #3c9aa8 100%);
  }

  .edge-stripe { position: absolute; left: 0; top: 0; width: 17px; height: 564px; background: var(--corp-purple); }

  .shapes { position: absolute; inset: 0; }

  .brand { position: absolute; left: 58px; top: 36px; display: flex; align-items: center; gap: 14px; }
  .brand-dot { width: 58px; height: 58px; border-radius: 50%; background: var(--corp-blue); }
  .brand-name { font-weight: 700; font-size: 52px; color: var(--ink); letter-spacing: 1px; line-height: 1; }

  .headline-band {
    position: absolute; left: 340px; top: 36px; width: 860px; height: 62px;
    background: var(--band-blue);
  }
  .headline {
    position: absolute; left: 477px; top: 52px;
    font-weight: 900; font-style: italic; font-size: 33px; line-height: 38px; color: var(--navy-ink);
    letter-spacing: 0.2px; white-space: nowrap;
  }
  .tagline {
    position: absolute; left: 491px; top: 98px; width: 587px; height: 26px;
    background: var(--white); border-radius: 0 0 16px 16px;
    font-weight: 300; font-size: 15.7px; color: var(--ink); white-space: nowrap;
    display: flex; align-items: center; justify-content: center;
  }

  .unique { position: absolute; left: 50px; top: 148px; width: 270px; color: var(--ink); }
  .unique-title { font-weight: 900; font-style: italic; font-size: 22px; color: var(--corp-purple); margin-bottom: 16px; white-space: nowrap; }
  .unique-item { font-weight: 300; font-size: 15.8px; line-height: 18.5px; margin-bottom: 16px; }
  .unique-item strong { font-weight: 500; }
  .unique-item .motto { display: block; font-weight: 500; font-size: 11px; line-height: 16px; white-space: nowrap; }

  .panel {
    position: absolute; border: 2px solid rgba(255,255,255,0.85); border-radius: 34px;
    color: var(--white); padding: 52px 4px 0 22px;
  }
  .panel-capabilities { left: 335px; top: 205px; width: 186px; height: 243px; background: var(--box-blue); }
  .panel-services { left: 646px; top: 196px; width: 186px; height: 173px; background: var(--box-purple); padding-top: 53px; padding-left: 18px; }
  .panel-markets { left: 915px; top: 205px; width: 186px; height: 243px; background: var(--box-blue); padding-top: 51px; padding-left: 17px; }
  .panel-title { font-weight: 500; font-size: 13.8px; margin-bottom: 13px; letter-spacing: 0.2px; white-space: nowrap; }
  .panel-list { list-style: none; font-weight: 300; font-size: 13px; line-height: 15.3px; white-space: nowrap; }
  .panel-list li::before { content: "• "; font-size: 9px; vertical-align: 2px; }
  .panel-list .wrap { padding-left: 10px; }

  .values-band {
    position: absolute; left: 17px; top: 492px; width: 248px; height: 28px;
    background: var(--band-blue); border-radius: 0 16px 16px 0;
  }
  .values-title {
    position: absolute; left: 56px; top: 492px; white-space: nowrap;
    font-weight: 900; font-style: italic; font-size: 24px; color: var(--corp-purple); line-height: 28px;
  }
  .value {
    position: absolute; top: 488px; width: 125px; height: 36px; border-radius: 16px;
    display: flex; align-items: center; justify-content: center; text-align: center;
    font-weight: 500; font-size: 16px; line-height: 14.5px;
  }
  .value-blue { background: var(--sky-blue); color: var(--navy-ink); }
  .value-purple { background: var(--corp-purple); color: var(--white); }
</style>
</head>
<body>
<main class="mural">
  <div class="skyline-scene" role="img" aria-label="City skyline at sunset with a tall observation tower, downtown high-rises and a domed stadium reflected in the lake"></div>

  <svg class="shapes" width="1200" height="564" viewBox="0 0 1200 564" aria-hidden="true">
    <defs>
      <linearGradient id="teal-sweep" x1="0" y1="0" x2="1" y2="1">
        <stop offset="0" stop-color="#35d3d6" stop-opacity="0.9"/>
        <stop offset="1" stop-color="#1fb2c4" stop-opacity="0.95"/>
      </linearGradient>
    </defs>
    <path d="M1200,258 C1140,280 1100,330 1095,400 C1090,470 1080,520 1062,564 L1200,564 Z" fill="url(#teal-sweep)"/>
    <path d="M17,0 L445,0 C360,50 320,160 302,300 C290,400 240,500 150,564 L17,564 Z" fill="#f3f4f7" fill-opacity="0.93"/>
    <path d="M17,2 L445,2" stroke="#574aa0" stroke-width="3"/>
    <path d="M445,0 C360,50 320,160 302,300 C290,400 240,500 150,564" fill="none" stroke="#574aa0" stroke-width="6"/>
    <path d="M458,0 C375,55 335,165 318,305 C306,405 260,505 178,564" fill="none" stroke="#1f4e9c" stroke-width="4"/>
  </svg>

  <div class="edge-stripe"></div>

  <div class="brand">
    <span class="brand-dot"></span>
    <span class="brand-name">QPT</span>
  </div>

  <div class="headline-band"></div>
  <h1 class="headline">Enabling Solutions for a Connected World</h1>
  <p class="tagline">We Distribute Products and Solution Services for Digital Infrastructure</p>

  <section class="unique">
    <h2 class="unique-title">What Makes Us Unique?</h2>
    <p class="unique-item"><strong>QPT Touch:</strong> We are more<br>than a catalog.</p>
    <p class="unique-item"><strong>QPT Experience:</strong> A pleasure<br>to do business with.
      <span class="motto">Proactive, Professional and Precise.</span></p>
    <p class="unique-item"><strong>QPT Solution:</strong> Design,<br>Develop, and Deliver<br>Custom Solutions; On-Time<br>and On-Spec</p>
  </section>

  <section class="panel panel-capabilities">
    <h3 class="panel-title">Our Capabilities</h3>
    <ul class="panel-list">
      <li>Wireless Infrastructure</li>
      <li>Broadband &amp; Fiber</li>
      <li>Site Solutions</li>
      <li>Fixed Wireless Access</li>
      <li>Test &amp; Measurement</li>
      <li>DAS &amp; PWN</li>
      <li>Power Solutions</li>
    </ul>
  </section>

  <section class="panel panel-services">
    <h3 class="panel-title">Solutions Services</h3>
    <ul class="panel-list">
      <li>Kitting &amp; Logistics</li>
      <li>Professional Engineering</li>
      <li>Placeholder</li>
    </ul>
  </section>

  <section class="panel panel-markets">
    <h3 class="panel-title">Our Markets</h3>
    <ul class="panel-list">
      <li>Carriers &amp; Cable<br><span class="wrap">Companies</span></li>
      <li>Data Centers</li>
      <li>Utilities</li>
      <li>Federal Government</li>
      <li>Education</li>
      <li>Industrial Manufacturing<br>&amp; Digital Supply Chain</li>
    </ul>
  </section>

  <div class="values-band"></div>
  <h2 class="values-title">Our Core Values</h2>
  <div class="value value-blue" style="left:290px">People First</div>
  <div class="value value-purple" style="left:434px">Intellectual<br>Curiosity</div>
  <div class="value value-blue" style="left:579px">Continuous<br>Improvement</div>
  <div class="value value-purple" style="left:720px">Customer<br>Focus</div>
  <div class="value value-blue" style="left:868px">Results<br>Matter</div>
</main>
</body>
</html>
```